Dual (Twin) Wet Wipe Packaging

We are a NY Based Hygiene Brand Specifically for couples, Creating Dual products for Him and Her,
Brand Name is quelvin.
Our Initial Product is a single Wet wipe Dual Package with perforated lines one wipe for him and one for her used for after sex.
We Would like to see designs that show a bold modern design with slight edgy to bring out the fun!
The final design Should bring out the idea of couples, connection and bond,

Attached Are photos of color ideas And Attached Design ideas.

The measurement of each half should be 7*9 cm total 14*9 cm with both attached.

```html
<!DOCTYPE html>
<html lang="en">
<head>
<meta charset="utf-8">
<title>quelvin – For Him / For Her Wet Wipe Sachet</title>
<link rel="stylesheet" href="https://fonts.googleapis.com/css2?family=Montserrat:wght@500;800&family=Open+Sans:wght@700&display=swap">
<style>
  :root {
    --canvas: #ffffff;
    --frame-line: #4a4a4a;
    --shadow: #d2d2d2;
    --him-seal: #62b3d8;
    --him-panel: #9ad2ea;
    --him-panel-deep: #67aed2;
    --him-accent: #229bd2;
    --her-seal: #dc377b;
    --her-panel: #f75f9a;
    --her-panel-deep: #ef2f7f;
    --her-accent: #dc377b;
    --her-soft: #f6a5c8;
    --ink: #2f2f2f;
    --white: #fafafc;
  }
  * { margin: 0; padding: 0; box-sizing: border-box; }
  html, body { width: 1200px; height: 773px; overflow: hidden; background: var(--canvas); }
  .canvas {
    position: relative; width: 1200px; height: 773px;
    background: var(--canvas); border: 1.5px solid var(--frame-line);
  }
  .sachet {
    position: absolute; left: 110px; top: 71px; width: 980px; height: 630px;
    box-shadow: 18px 14px 8px var(--shadow);
  }
  .sachet-art { position: absolute; inset: 0; width: 980px; height: 630px; }
  .notch {
    position: absolute; top: 95px; width: 14px; height: 14px;
    border-radius: 50%; background: var(--canvas);
  }
  .notch--left { left: -7px; }
  .notch--right { right: -7px; }
  .label {
    position: absolute; line-height: 1; text-align: center; white-space: nowrap;
    font-family: "Montserrat", sans-serif;
  }
  .label--for { font-weight: 800; font-size: 90px; top: 280px; width: 400px; }
  .label--who { font-weight: 800; font-size: 137px; top: 345px; width: 440px; color: var(--white); }
  .label--kind { font-weight: 500; font-size: 38px; top: 522px; width: 300px; }
  .him { left: 60px; }
  .her { left: 491px; }
  .label--for.him { color: var(--him-accent); }
  .label--for.her { color: var(--her-accent); }
  .label--kind.him { left: 118px; color: var(--ink); }
  .label--kind.her { left: 562px; color: var(--her-soft); }
  .label--who.him { left: 40px; }
  .label--who.her { left: 491px; }
  .brand-name {
    position: absolute; left: 340px; top: 192px; width: 300px;
    text-align: center; line-height: 1;
    font-family: "Open Sans", sans-serif; font-weight: 700; font-size: 39px;
    color: var(--white); letter-spacing: 0.5px; text-transform: uppercase;
  }
  .motif { position: absolute; }
  .motif--heart { left: 90px; top: 88px; width: 64px; height: 51px; background: var(--him-accent); border-radius: 40% 40% 50% 50%; }
  .motif--planet { left: 212px; top: 184px; width: 97px; height: 47px; background: var(--white); border-radius: 50%; opacity: .85; }
  .motif--spark-him { left: 67px; top: 516px; width: 45px; height: 46px; background: var(--him-accent); border-radius: 50%; opacity: .6; }
  .motif--lips { left: 754px; top: 57px; width: 136px; height: 88px; background: var(--her-soft); border-radius: 50%; opacity: .85; }
  .motif--cherry { left: 657px; top: 153px; width: 79px; height: 83px; background: var(--her-soft); border-radius: 40%; opacity: .85; }
  .motif--spark-a { left: 594px; top: 61px; width: 36px; height: 36px; background: var(--her-soft); border-radius: 50%; opacity: .6; }
  .motif--spark-b { left: 827px; top: 188px; width: 53px; height: 55px; background: var(--her-soft); border-radius: 50%; opacity: .6; }
  .motif--spark-c { left: 861px; top: 513px; width: 42px; height: 43px; background: var(--her-soft); border-radius: 50%; opacity: .6; }
</style>
</head>
<body>
<main class="canvas">
  <section class="sachet">
    <svg class="sachet-art" viewBox="0 0 980 630" aria-hidden="true">
      <defs>
        <linearGradient id="him-panel-fade" x1="0" y1="0" x2="0" y2="1">
          <stop offset="0.83" stop-color="var(--him-panel)"/>
          <stop offset="1" stop-color="var(--him-panel-deep)"/>
        </linearGradient>
        <linearGradient id="her-panel-side" x1="0" y1="0" x2="1" y2="0">
          <stop offset="0.72" stop-color="var(--her-panel)"/>
          <stop offset="1" stop-color="var(--her-panel-deep)"/>
        </linearGradient>
        <linearGradient id="her-panel-base" x1="0" y1="0" x2="0" y2="1">
          <stop offset="0.8" stop-color="var(--her-panel-deep)" stop-opacity="0"/>
          <stop offset="1" stop-color="var(--her-panel-deep)" stop-opacity="0.7"/>
        </linearGradient>
        <pattern id="perforation" x="0" y="0" width="6" height="9" patternUnits="userSpaceOnUse">
          <polygon points="0,0 6,4.5 0,9" fill="var(--him-seal)"/>
        </pattern>
        <pattern id="perforation-inner" x="0" y="0" width="6" height="9" patternUnits="userSpaceOnUse">
          <polygon points="0,0 6,4.5 0,9" fill="var(--him-panel)"/>
        </pattern>
      </defs>
      <rect class="seal seal--him" x="0" y="0" width="490" height="630" fill="var(--him-seal)"/>
      <rect class="seal seal--her" x="490" y="0" width="490" height="630" fill="var(--her-seal)"/>
      <rect class="panel panel--him" x="45" y="36" width="445" height="556" fill="url(#him-panel-fade)"/>
      <rect class="panel panel--her" x="490" y="36" width="436" height="556" fill="url(#her-panel-side)"/>
      <rect class="panel-base panel-base--her" x="490" y="36" width="436" height="556" fill="url(#her-panel-base)"/>
      <rect class="perforation" x="490" y="0" width="6" height="630" fill="url(#perforation)"/>
      <rect class="perforation" x="490" y="36" width="6" height="500" fill="url(#perforation-inner)"/>
    </svg>
    <span class="notch notch--left"></span>
    <span class="notch notch--right"></span>

    <div class="motif motif--heart" role="img" aria-label="Small heart icon"></div>
    <div class="motif motif--planet" role="img" aria-label="Ringed planet illustration"></div>
    <div class="motif motif--spark-him" role="img" aria-label="Sparkle ornament"></div>
    <div class="motif motif--spark-a" role="img" aria-label="Sparkle ornament"></div>
    <div class="motif motif--lips" role="img" aria-label="Lipstick kiss print illustration"></div>
    <div class="motif motif--cherry" role="img" aria-label="Cherry pair illustration"></div>
    <div class="motif motif--spark-b" role="img" aria-label="Sparkle ornament"></div>
    <div class="motif motif--spark-c" role="img" aria-label="Sparkle ornament"></div>

    <p class="brand-name">quelvin</p>

    <h2 class="label label--for him">FOR</h2>
    <h2 class="label label--who him">HIM</h2>
    <p class="label label--kind him">WET WIPE</p>

    <h2 class="label label--for her">FOR</h2>
    <h2 class="label label--who her">HER</h2>
    <p class="label label--kind her">WET WIPE</p>
  </section>
</main>
</body>
</html>
```